Say Something About Privacy!!!

We need a poster designed with the theme of "Privacy". With so many digital assistants (Vonu, Marvo, Plinker, etc) listening to our conversations and web cams watching our activities privacy is becoming more important than ever. The goal of the project is to design a poster that can be used as giveaway item at trade shows, etc. The poster should be engaging and thought provoking. The tone can be serious or lighthearted. You can use a photo, illustration, or just copy to get your point across. I've included a few examples of other posters I like.

Target Market(s)

General Public. Well educated. Tech enthusiasts. People with smartphones and/or smart speakers.

Industry/Entity Type

Cyber Security

Font styles to use
Sans Serif

Requirements
Must have
• Simple design. Strong colours.
Should not have
• While this is a serious subject, I don't want the message to be too threatening.

```html
<!DOCTYPE html>
<html lang="en">
<head>
<meta charset="UTF-8">
<title>Privacy on the Internet</title>
<link rel="stylesheet" href="https://fonts.googleapis.com/css2?family=Stardos+Stencil:wght@700&family=Oswald:wght@600&display=swap">
<style>
  :root {
    --page-bg: #8a8a8a;
    --poster-dark: #141414;
    --poster-mid: #2a2a2a;
    --ink: #f4f4f2;
    --ink-soft: #dcdcda;
  }
  html, body {
    margin: 0;
    padding: 0;
    width: 1200px;
    height: 845px;
    overflow: hidden;
    background: var(--page-bg);
  }
  .poster {
    position: absolute;
    left: 322px;
    top: 22px;
    width: 556px;
    height: 800px;
    background: radial-gradient(ellipse at 45% 55%, var(--poster-mid) 0%, var(--poster-dark) 75%);
    color: var(--ink);
  }
  .lock-artwork {
    position: absolute;
    left: 189px;
    top: 80px;
    width: 179px;
    height: 214px;
    border-radius: 6px;
    background: linear-gradient(180deg, var(--ink) 0%, var(--ink-soft) 100%);
  }
  .headline {
    position: absolute;
    left: 0;
    right: 0;
    top: 330px;
    margin: 0;
    text-align: center;
    font-family: "Stardos Stencil", sans-serif;
    font-weight: 700;
    font-size: 100px;
    line-height: 111px;
    letter-spacing: 1px;
    text-transform: uppercase;
    white-space: nowrap;
  }
  .headline span { display: block; }
  .tagline {
    position: absolute;
    left: 88px;
    top: 662px;
    width: 379px;
    height: 53px;
    box-sizing: border-box;
    border: 2px solid var(--ink);
    display: flex;
    align-items: center;
    justify-content: center;
    margin: 0;
    font-family: "Oswald", sans-serif;
    font-weight: 600;
    font-size: 28px;
    letter-spacing: 1.5px;
    text-transform: uppercase;
    white-space: nowrap;
  }
</style>
</head>
<body>
  <main class="poster">
    <div class="lock-artwork" role="img" aria-label="Distressed white padlock artwork"></div>
    <h1 class="headline">
      <span>Privacy</span>
      <span>On the</span>
      <span>Internet</span>
    </h1>
    <p class="tagline">That’s an oxymoron</p>
  </main>
</body>
</html>
```